New profile page for existing party website

For the party website 'Brindlepost' we need a new design for the user profile page.

The page should show
* a profile picture
* basic information like name, age and city
* music styles he/she likes
* links to their Friendwall profile and website
* a bio (HTML content)
* events they plan to go to
* past events
* pictures

Challenge is that some users may have little information (just their name) while others have a huge description, lots of foto's, events, etc.

Please visit http://www.brindlepost.example and http://www.brindlepost.example/users/tobias

Target Market(s)

Men and women between 18 and 35

Industry/Entity Type

Night Club

Number of Pages Required

2 page

Font styles to use
Other font styles liked:
• Roboto

Requirements
Must have
• Please design how the page looks with a fully filled out profile and with an empty profile.
• It should fit well with the existing website.
• Include designs for both for small screens (mobile) and large screens (tablet, desktop).
Nice to have
• UX design on how to collapse or paginate sections.
• Interactive effects would be a bonus.
Should not have
• The page should not have subnavigation like menus or tabs.

```html
<!DOCTYPE html>
<html lang="en">
<head>
<meta charset="utf-8">
<title>Tobias Marlow – Brindlepost</title>
<link href="https://fonts.googleapis.com/css2?family=Lato:wght@300;400;700&display=swap" rel="stylesheet">
<style>
:root{
  --page:#333333;
  --sidebar:#2b2b2b;
  --footer:#232323;
  --rule:#cfcfcf;
  --white:#ffffff;
  --card:#fdfdfd;
  --accent:#12c488;
  --muted:#757575;
  --dot:#cfcfcf;
  --ink:#1c1c1c;
  --gold:#c9982e;
}
*{box-sizing:border-box;margin:0;padding:0}
html,body{width:1200px;height:582px;overflow:hidden}
body{background:var(--page);font-family:"Lato",sans-serif;position:relative;color:var(--white)}

.sidebar{position:absolute;left:0;top:0;width:188px;height:582px;background:var(--sidebar)}
.avatar{position:absolute;left:47px;top:23px;width:94px;height:94px;border-radius:50%;background:radial-gradient(circle at 50% 40%,#8a5a3c,#4a2f22 70%,#a36b2e)}
.profile-name{position:absolute;left:0;width:188px;top:130px;text-align:center;font-weight:300;font-size:22px}
.section-rule{position:absolute;left:8px;width:172px;height:1px;background:var(--rule)}
.sidebar-heading{position:absolute;left:0;width:188px;top:237px;text-align:center;font-weight:300;font-size:13.5px;color:#cfcfcf}
.video-thumb{position:absolute;left:7px;top:306px;width:171px;height:140px;background:linear-gradient(180deg,#8d9db3 0%,#4f5a6e 40%,#1e2230 100%)}
.play-button{position:absolute;left:78px;top:63px;width:16px;height:12px;border-radius:3px;background:rgba(0,0,0,.75)}
.social-bar{position:absolute;left:0;bottom:0;width:188px;height:33px;background:var(--footer);display:flex;justify-content:space-around;align-items:center;font-size:9px;color:#ddd;font-weight:700}

.main-title{position:absolute;left:288px;top:20px;font-weight:300;font-size:18px}
.main-rule{position:absolute;left:287px;top:56px;width:800px;height:1px;background:var(--rule)}

.timeline-line{position:absolute;left:498px;top:132px;width:5px;height:378px;background:var(--white)}
.event-date{position:absolute;left:418px;width:81px;height:30px;background:var(--accent);font-size:11.5px;display:flex;align-items:center;justify-content:center}
.event-dot{position:absolute;left:494px;width:13px;height:13px;border-radius:50%;background:var(--dot);border:2px solid var(--white)}
.event-dot.active{background:var(--white);border:3px solid var(--accent)}
.event-card{position:absolute;left:519px;width:432px;background:var(--card);border-left:6px solid var(--accent);border-radius:0 3px 3px 0;box-shadow:0 2px 2px rgba(0,0,0,.35)}
.event-title{position:absolute;left:22px;font-size:13.5px;color:var(--muted)}
.event-image{position:absolute;left:22px;top:43px;width:48px;height:47px;border:1px solid #ddd;background:#fff;display:flex;align-items:center;justify-content:center}
.event-image span{width:38px;height:38px;border-radius:50%;background:radial-gradient(circle at 40% 40%,#e8c268,var(--gold))}
.event-text{position:absolute;left:92px;top:44px;width:326px;font-size:10.2px;line-height:15px;color:var(--ink)}
</style>
</head>
<body>
<aside class="sidebar">
  <div class="avatar" role="img" aria-label="Profile photo of Tobias Marlow"></div>
  <h1 class="profile-name">Tobias Marlow</h1>
  <div class="section-rule" style="top:222px"></div>
  <h2 class="sidebar-heading">Video Gallery</h2>
  <div class="section-rule" style="top:268px"></div>
  <div class="video-thumb" role="img" aria-label="Video still of a crowd at an outdoor dance festival"><span class="play-button"></span></div>
  <nav class="social-bar"><span>Friendwall</span><span>Chirpline</span><span>Workgrid</span></nav>
</aside>

<h2 class="main-title">Past Events</h2>
<div class="main-rule"></div>

<div class="timeline-line"></div>

<div class="event-date" style="top:147px">Mar 2016</div>
<div class="event-dot active" style="top:156px"></div>
<article class="event-card" style="top:140px;height:146px">
  <h3 class="event-title" style="top:15px">Brindlepost Event March 2016</h3>
  <div class="event-image" role="img" aria-label="Event image: gold medal"><span></span></div>
  <p class="event-text">Lorem ipsum dolor sit amet, consectetur adipiscing elit. Sed egestas dapibus lectus non dignissim. Pellentesque auctor ornare urna, volutpat condimentum quam porttitor at. Vestibulum tincidunt diam in eros aliquam luctus. Donec sagittis a purus a porttitor. Sed non feugiat enim. Donec eget metus erat. Vivamus sed consequat orci. Aenean commodo lectus sed purus auctor ullamcorper.</p>
</article>

<div class="event-date" style="top:303px">Jan 2016</div>
<div class="event-dot" style="top:311px"></div>
<article class="event-card" style="top:294px;height:47px"><h3 class="event-title" style="top:15px">Brindlepost Event January 2016</h3></article>

<div class="event-date" style="top:356px">June 2015</div>
<div class="event-dot" style="top:364px"></div>
<article class="event-card" style="top:348px;height:46px"><h3 class="event-title" style="top:15px">Brindlepost Event June 2015</h3></article>

<div class="event-date" style="top:410px">May 2015</div>
<div class="event-dot" style="top:418px"></div>
<article class="event-card" style="top:402px;height:46px"><h3 class="event-title" style="top:15px">Brindlepost Event May 2015</h3></article>

<div class="event-date" style="top:464px">Aug 2014</div>
<div class="event-dot" style="top:472px"></div>
<article class="event-card" style="top:456px;height:46px"><h3 class="event-title" style="top:15px">Brindlepost Event August 2014</h3></article>
</body>
</html>
```